Harbinger Noble Alloys Works Business Cards

We are wanting to have a new business card designed for our company as we go to a convention. We want to balance business/Modern with elegance and beauty. Our company sells highend jewelry pieces. We want to utilize the colors of Black and Gold and have gold foiled fonts to be physically printed on the business cards.
We also would like to have space to write notes on the back side of the business card. When we meet people at jewelry conventions we would like to write notes if possible.
Here are websites and designs that we like the look and feel of these companies and you can use these as design ideas.
https://www.lorvanne.com
https://www.bellquist.com/en-us/home
Here is our company website link
www.harbingernaw.com
I also up loaded two versions of our logo.
- Update 4.26.22
I have uploaded photos of a business card we like. this card has raised embossed letters that you can feel. the raise letters are like a plastic but we don't need to use that...I uploaded to show you that we like the experience of the client feeling the characters of the logo. we also would like to have the material as a satin or some material very soft.
- Maybe we can get designs with beautiful gold foiling and raised characters and logos. we like simplicity...not busy but an elegant design. We need to write notes and would like a section where we can write notes. but we want an elegant style and the client has an experience with the feel of the card when they touch the card.
Colors
- Main colors Black & Gold
- white or light colors for small notes section.
Specialty ideals and things we would like to see based on your design styles.
- raised fonts
- raised logos
- gold foiling
- satin/soft finish on the card material.
we are wanting to design a business card that looks elegant and clean. When the client is handed the business card we want them to physically experience the business card as well by touching the raised logos or fonts and the base material is soft satin. I hope this helps with further designs.
thank you all
We uploaded a new contact layout that we have designed in our office. we would like to see how this would look on your designs.
thank you
I just finished uploading the Contact Layout. the colors are just examples. please use this layout as an idea and use colors based on the feed back we have given each of you personally.
Contact Information for Business Card
we need an area to write notes, we would like to have our logos or the diamond of our logo or the business card to have embossed sections to the business card so when the customer touches the card they can feel the logo. we would also like sections of our business card to have gold foiling. we would also like to use a satin soft paper with our card. when the client touches the card its super soft and high quality
Requirements
Must have
- we would like to have our logos or the diamond of our logo or the business card to have embossed sections to the business card so when the customer touches the card they can feel the logo. we would also like sections of our business card to have gold foiling. we would also like to use a satin soft paper with our card. when the client touches the card its super soft and high quality
Nice to have
- we would like to have our logos or the diamond of our logo or the business card to have embossed sections to the business card so when the customer touches the card they can feel the logo. we would also like sections of our business card to have gold foiling.

```html
<!DOCTYPE html>
<html lang="en">
<head>
<meta charset="utf-8">
<title>Harbinger Noble Alloys Works — Business Card</title>
<link href="https://fonts.googleapis.com/css2?family=Cinzel:wght@400&family=Montserrat:wght@400;500&display=swap" rel="stylesheet">
<style>
  :root {
    --backdrop: #ececec;
    --card-black: #141414;
    --card-black-edge: #0c0c0c;
    --gold: #c9a04a;
    --gold-light: #e2c27a;
    --gold-deep: #9c7a30;
    --ivory: #ffffff;
    --line-grey: #d9d9d9;
    --label-grey: #9a9a9a;
    --text-light: #e9e6df;
  }
  * { box-sizing: border-box; margin: 0; padding: 0; }
  html, body { width: 800px; height: 1200px; overflow: hidden; }
  body {
    background: var(--backdrop);
    font-family: "Montserrat", sans-serif;
    display: flex;
    flex-direction: column;
    align-items: center;
    justify-content: center;
    gap: 60px;
  }
  .card {
    width: 640px;
    height: 366px;
    box-shadow: 0 6px 18px rgba(0,0,0,0.18);
    position: relative;
    overflow: hidden;
  }

  /* Front */
  .card-front {
    background: radial-gradient(ellipse at 50% 40%, var(--card-black) 0%, var(--card-black-edge) 100%);
    display: flex;
    flex-direction: column;
    align-items: center;
    color: var(--text-light);
  }
  .brand-mark {
    width: 22px; height: 22px;
    border-radius: 50%;
    background: var(--gold);
    margin-top: 86px;
  }
  .brand-name {
    font-family: "Cinzel", serif;
    font-weight: 400;
    font-size: 34px;
    letter-spacing: 1px;
    color: var(--text-light);
    margin-top: 14px;
  }
  .brand-tagline {
    font-family: "Cinzel", serif;
    font-size: 22px;
    letter-spacing: 1px;
    color: var(--text-light);
    margin-top: 4px;
  }
  .flourish {
    width: 70px; height: 14px;
    margin-top: 44px;
    background: linear-gradient(90deg, transparent, var(--gold-deep), var(--gold-light), var(--gold-deep), transparent);
    border-radius: 7px;
    opacity: 0.8;
  }
  .front-web {
    font-size: 16px;
    font-weight: 500;
    letter-spacing: 4px;
    color: var(--gold);
    margin-top: 18px;
  }

  /* Back */
  .card-back { display: flex; background: var(--ivory); }
  .contact-panel {
    width: 308px;
    background: var(--card-black);
    padding: 72px 0 0 30px;
    color: var(--text-light);
  }
  .contact-panel .brand-name { font-size: 17px; margin-top: 0; }
  .contact-panel .brand-tagline { font-size: 11px; margin-top: 2px; }
  .contact-list { list-style: none; margin-top: 26px; }
  .contact-item {
    display: flex; align-items: center; gap: 12px;
    font-size: 11px; color: var(--text-light);
    margin-bottom: 14px;
    line-height: 1.35;
  }
  .contact-item.address { font-size: 8.5px; }
  .contact-icon {
    width: 18px; height: 18px; flex: none;
    border-radius: 50%; background: var(--gold);
    display: flex; align-items: center; justify-content: center;
  }
  .contact-icon svg { width: 10px; height: 10px; }
  .gold-stripe {
    width: 8px;
    background: linear-gradient(180deg, var(--gold-deep), var(--gold-light), var(--gold-deep));
  }
  .notes-panel { flex: 1; padding: 38px 30px 0 28px; position: relative; }
  .notes-label {
    font-size: 11px; letter-spacing: 2px; color: var(--label-grey);
    font-weight: 500;
  }
  .notes-lines { margin-top: 10px; }
  .notes-line { height: 42px; border-bottom: 1px solid var(--line-grey); }
  .faint-mark {
    position: absolute; right: 18px; top: 14px;
    width: 96px; height: 96px; border-radius: 50%;
    background: #f1f1f1;
    z-index: 0;
  }
  .notes-label, .notes-lines { position: relative; z-index: 1; }
</style>
</head>
<body>

  <section class="card card-front" aria-label="Business card front">
    <div class="brand-mark"></div>
    <div class="brand-name">Harbinger Noble Alloys Works</div>
    <div class="brand-tagline">— Coins, Jewelry &amp; Diamonds —</div>
    <div class="flourish" role="img" aria-label="Gold foil ornamental flourish"></div>
    <div class="front-web">www.harbingernaw.com</div>
  </section>

  <section class="card card-back" aria-label="Business card back">
    <div class="contact-panel">
      <div class="brand-name">Harbinger Noble Alloys Works</div>
      <div class="brand-tagline">— Coins, Jewelry &amp; Diamonds —</div>
      <ul class="contact-list">
        <li class="contact-item">
          <span class="contact-icon"><svg viewBox="0 0 10 10"><path d="M2 1l2 2-1 1.2c.6 1.2 1.5 2.1 2.8 2.8L7 6l2 2-1.2 1.2C4.5 9 1 5.5.8 2.2z" fill="#141414"/></svg></span>
          (555) 014-2290
        </li>
        <li class="contact-item address">
          <span class="contact-icon"><svg viewBox="0 0 10 10"><path d="M5 .8a3 3 0 0 1 3 3c0 2.2-3 5.6-3 5.6S2 6 2 3.8a3 3 0 0 1 3-3z" fill="#141414"/><circle cx="5" cy="3.8" r="1" fill="#c9a04a"/></svg></span>
          88 Quarry Lane NE<br>Fenwick, Oregon USA 97000
        </li>
        <li class="contact-item">
          <span class="contact-icon"><svg viewBox="0 0 10 10"><rect x="1" y="2.2" width="8" height="5.6" fill="none" stroke="#141414" stroke-width="1"/><path d="M1 2.4l4 3 4-3" fill="none" stroke="#141414" stroke-width="1"/></svg></span>
          info@harbingernaw.com
        </li>
        <li class="contact-item">
          <span class="contact-icon"><svg viewBox="0 0 10 10"><circle cx="5" cy="5" r="3.8" fill="none" stroke="#141414" stroke-width="1"/><path d="M1.2 5h7.6M5 1.2c-2 2.4-2 5.2 0 7.6M5 1.2c2 2.4 2 5.2 0 7.6" fill="none" stroke="#141414" stroke-width=".8"/></svg></span>
          www.harbingernaw.com
        </li>
      </ul>
    </div>
    <div class="gold-stripe"></div>
    <div class="notes-panel">
      <div class="faint-mark"></div>
      <div class="notes-label">NOTES</div>
      <div class="notes-lines">
        <div class="notes-line"></div>
        <div class="notes-line"></div>
        <div class="notes-line"></div>
        <div class="notes-line"></div>
        <div class="notes-line"></div>
        <div class="notes-line"></div>
      </div>
    </div>
  </section>

</body>
</html>
```